Business Card/ Email Signature Design Project

I am an Interior Designer. I need a business card that looks sophisticated stylish but simple in design. My work covers space design/ interior architecture/ furniture design/ product development & styling.

I have a very specific brief and know mostly what I want. I'm hoping to work with someone who can translate my ideas.

My branding should have a strong focus on my name, the majority of my work is referral based.
I'm keen to keep a monochromatic colour scheme: dark charcoal/ black/ white/ embossing/ silver. I'm not suggesting we use all that I've listed, they are possible ideas at this stage. I will need to be mindful of printing costs an also how I make the design work across, cards, letter heads, email logo and web design.

Theory behind images sent below;
1-Rug Image_(minus boarder) I was thinking this image could be used on the back of the card with my contact details over. I like that the lines are almost hand drawn and start to look free form. It's a subtle contrast to a more formal front of the card with my name.
2_Tomas Ferle_I really like the orientation, the proportion of font on the card, the colour and the font. I like the lower case for my name and the upper case for 'Interior Design'. Not sure if it should be 'Interior Designer or Interior Design' at this stage, was leaning towards 'Interior Design'. Was thinking the 'i' and 'd' in my surname could be the colour eg 'silver'?? We can decide on this once we see it.

Look forward to hearing from you.
Cheers,
Saskia Bremond

Printing

Saskia Bremond Interior Design

```html
<!DOCTYPE html>
<html lang="en">
<head>
<meta charset="utf-8">
<title>Saskia Bremond Interior Design — Business Card</title>
<link href="https://fonts.googleapis.com/css2?family=Arvo:wght@700&family=Cinzel:wght@400&family=Open+Sans:wght@400&display=swap" rel="stylesheet">
<style>
  :root {
    --page: #e9e7e3;
    --card-black: #111111;
    --card-charcoal: #262626;
    --ink-white: #f4f4f4;
    --ink-silver: #c9c9c9;
    --band: #4a4a4a;
  }
  * { margin: 0; padding: 0; box-sizing: border-box; }
  html, body {
    width: 1200px;
    height: 1023px;
    overflow: hidden;
    background: var(--page);
  }
  .sheet {
    width: 1200px;
    height: 1023px;
    display: flex;
    flex-direction: column;
    align-items: center;
    justify-content: center;
    gap: 60px;
  }
  .card {
    position: relative;
    width: 700px;
    height: 400px;
    border-radius: 4px;
    overflow: hidden;
    box-shadow: 0 10px 28px rgba(0,0,0,0.22);
  }

  /* Front */
  .card-front {
    background: linear-gradient(135deg, var(--card-charcoal) 0%, var(--card-black) 55%, #1b1b1b 100%);
  }
  .identity {
    position: absolute;
    left: 64px;
    top: 168px;
    display: flex;
    flex-direction: column;
    align-items: flex-end;
  }
  .identity-name {
    font-family: "Arvo", "Rockwell", serif;
    font-weight: 700;
    font-size: 62px;
    line-height: 1;
    letter-spacing: 0.5px;
    color: var(--ink-white);
  }
  .identity-title {
    margin-top: 8px;
    font-family: "Cinzel", "Trajan Pro", serif;
    font-weight: 400;
    font-size: 22px;
    letter-spacing: 1.5px;
    color: var(--ink-silver);
  }

  /* Back */
  .card-back .rug-texture {
    position: absolute;
    inset: 0;
    width: 100%;
    height: 100%;
  }
  .contact-band {
    position: absolute;
    right: 0;
    bottom: 70px;
    width: 330px;
    padding: 18px 28px;
    background: var(--band);
    font-family: "Open Sans", "Helvetica Neue", sans-serif;
    font-style: normal;
    font-weight: 400;
    font-size: 14px;
    line-height: 1.75;
    letter-spacing: 0.6px;
    color: var(--ink-white);
  }
  .contact-line { display: block; white-space: nowrap; }
</style>
</head>
<body>
  <main class="sheet">
    <section class="card card-front" aria-label="Business card front">
      <div class="identity">
        <h1 class="identity-name">saskia bremond</h1>
        <p class="identity-title">INTERIOR DESIGNER</p>
      </div>
    </section>

    <section class="card card-back" aria-label="Business card back">
      <svg class="rug-texture" role="img" aria-label="Grey rug texture with loose hand-drawn lines" viewBox="0 0 700 400" preserveAspectRatio="none">
        <defs>
          <linearGradient id="rugTone" x1="0" y1="0" x2="1" y2="1">
            <stop offset="0" stop-color="#c4c4c4"/>
            <stop offset="0.55" stop-color="#9a9a9a"/>
            <stop offset="1" stop-color="#6e6e6e"/>
          </linearGradient>
        </defs>
        <rect width="700" height="400" fill="url(#rugTone)"/>
      </svg>
      <address class="contact-band">
        <span class="contact-line">M 0412 558 903</span>
        <span class="contact-line">studio@saskiabremond.com</span>
        <span class="contact-line">14 Alder Lane, Wrenhille QLD 4817</span>
      </address>
    </section>
  </main>
</body>
</html>
```